Business card design for a content marketing agency

Need a business card design suitable for a digital marketing agency. Needs to be a bold and creative, high quality design that exudes expertise and professionalism, and instills in prospective new customers a sense of confidence that we are the right company to do business with. Specifications must meet PrintaLoom requirement for extra thick matte stock. Needs to incorporate logo, tagline, name, title, website url, address, city, state, zip code, and mobile number.. I spec'd s single side design but I'm to a double sided design if it's strong and compelling. I like the use of icons associated with contact info, but it's not a requirement. Mostly, the design needs to command attention because it's so good or unusual. I have all kinds of files in large thru small sizes in jpg andpgn. pick from what you need, and let me know if you have questions.

Target Market(s)

CEO, Mktg VP's and small to medium size tech and prof'l service businesses

Industry/Entity Type

Marketing

Contact Information for Business Card

Pedro Finch
Chief Executive Officer
487 Marrow Creek Lane
Harlow Falls, NH 03842
pedro@quenvelmedia.example
www.quenvelmedia.example
978-555-0163

Font styles to use
Sans Serif

Colors
0692cd
9bcb3c

Requirements
Must have
• Tagline is "Stories That Clients Believe".
• Needs to be a bold and creative, high quality design that exudes expertise and professionalism, and instills in prospective new customers a sense of confidence that we are the right company to do business with. Specifications must meet PrintaLoom requirement for extra thick matte stock. Needs to incorporate logo, tagline, name, title, website url, address, city, state, zip code, and mobile number..
Nice to have
• I spec'd s single side design but I'm open to a double sided design if it's strong and compelling. I like the use of icons associated with contact info, but it's not a requirement.
Should not have
• Chose colors that are the same and/or compatible with colors in the logo

```html
<!DOCTYPE html>
<html lang="en">
<head>
<meta charset="UTF-8">
<title>Quenvel Media — Business Card</title>
<link href="https://fonts.googleapis.com/css2?family=Open+Sans:wght@400;600;700&display=swap" rel="stylesheet">
<style>
  :root {
    --brand-blue: #0692cd;
    --ink: #1a1a1a;
    --card: #ffffff;
    --backdrop: #e6e8ea;
    --mark-blue: #2a9ad8;
  }
  * { box-sizing: border-box; margin: 0; padding: 0; }
  html, body {
    width: 1200px; height: 900px; overflow: hidden;
    background: var(--backdrop);
    font-family: "Open Sans", Arial, sans-serif;
  }
  .sheet {
    width: 1200px; height: 900px;
    display: flex; flex-direction: column; align-items: center; justify-content: center;
    gap: 40px;
  }
  .card {
    position: relative;
    width: 700px; height: 400px;
    background: var(--card);
    box-shadow: 0 6px 18px rgba(0,0,0,0.18);
  }
  /* Front */
  .front-brand {
    position: absolute; left: 0; right: 0; top: 120px;
    display: flex; align-items: center; justify-content: center; gap: 16px;
  }
  .brand-square {
    width: 34px; height: 34px; background: var(--mark-blue);
  }
  .front-brand .brand-name {
    font-size: 44px; font-weight: 600; color: var(--ink); letter-spacing: 0.5px;
  }
  .tagline {
    position: absolute; left: 0; right: 0; bottom: 52px;
    text-align: center;
    font-size: 15px; font-weight: 600; letter-spacing: 1.2px;
    color: var(--brand-blue); text-transform: uppercase;
  }
  /* Back */
  .back-brand {
    position: absolute; left: 58px; top: 250px;
    display: flex; align-items: center; gap: 12px;
  }
  .back-brand .brand-square { width: 26px; height: 26px; }
  .back-brand .brand-name {
    font-size: 34px; font-weight: 600; color: var(--ink);
  }
  .contact {
    position: absolute; left: 430px; top: 150px;
    color: var(--ink);
  }
  .contact-name {
    font-size: 27px; font-weight: 700; color: var(--brand-blue);
    text-transform: uppercase; letter-spacing: 0.5px; line-height: 1.1;
  }
  .contact-title {
    font-size: 13.5px; font-weight: 600; text-transform: uppercase; letter-spacing: 0.3px;
    margin-bottom: 6px;
  }
  .contact-address { font-size: 14px; line-height: 1.35; margin-bottom: 8px; }
  .contact-list { list-style: none; font-size: 14px; line-height: 1.5; }
  .contact-list li { display: flex; align-items: center; gap: 8px; }
  .contact-list svg { width: 12px; height: 12px; flex: none; }
</style>
</head>
<body>
<main class="sheet">
  <section class="card card-front">
    <div class="front-brand">
      <span class="brand-square"></span>
      <span class="brand-name">Quenvel Media</span>
    </div>
    <p class="tagline">Stories That Clients Believe</p>
  </section>

  <section class="card card-back">
    <div class="back-brand">
      <span class="brand-square"></span>
      <span class="brand-name">Quenvel Media</span>
    </div>
    <div class="contact">
      <h1 class="contact-name">Pedro Finch</h1>
      <p class="contact-title">Chief Executive Officer</p>
      <p class="contact-address">487 Marrow Creek Lane<br>Harlow Falls, NH 03842</p>
      <ul class="contact-list">
        <li>
          <svg viewBox="0 0 12 12" aria-hidden="true"><path d="M2.5 1 L4.5 1 L5.2 3.5 L4 4.5 Q5 7 7.5 8 L8.5 6.8 L11 7.5 L11 9.5 Q10.5 11 9 11 Q1 10 1 3 Q1 1.5 2.5 1Z" fill="var(--brand-blue)"/></svg>
          978-555-0163
        </li>
        <li>
          <svg viewBox="0 0 12 12" aria-hidden="true"><rect x="1" y="2.5" width="10" height="7" fill="none" stroke="var(--brand-blue)" stroke-width="1.2"/><path d="M1 2.5 L6 6.5 L11 2.5" fill="none" stroke="var(--brand-blue)" stroke-width="1.2"/></svg>
          pedro@quenvelmedia.example
        </li>
        <li>
          <svg viewBox="0 0 12 12" aria-hidden="true"><circle cx="6" cy="6" r="5" fill="none" stroke="var(--brand-blue)" stroke-width="1.1"/><ellipse cx="6" cy="6" rx="2.2" ry="5" fill="none" stroke="var(--brand-blue)" stroke-width="1"/><path d="M1 6 H11" stroke="var(--brand-blue)" stroke-width="1"/></svg>
          www.quenvelmedia.example
        </li>
      </ul>
    </div>
  </section>
</main>
</body>
</html>
```